依頼詳細
自社に関わってくださっている顧客の皆様と各企業様あてに感謝が伝えられるような年賀状を作っていただきたいと思っています。
記載項目
前年に同じ
希望イメージ
シンプル 複雑
単色 カラフル
暗い 明るい
日常 高級
遊び心 厳粛
未来的 伝統的
女性的 男性的
希望する色
赤系
納品ファイル
• 高解像度JPG (.jpg)
• イラストレーター形式 (.ai)
• フォトショップ形式 (.psd)
• PNG形式 (.png)
補足説明
たくさんの応募ありがとうございます。
どの作品も素敵なのですが過去に扱ったデザインと似たものが多く決定に至りません。
そこで我が社のロゴをメインにした年賀状にしてみたらと考えなおしたのですが可能でしょうか。
お手数をおかけしますが何卒よろしくお願い申し上げます。
今月末までの締め切り日に変更させていただきました。
■ 選んだ理由

シンプルかつ爽やかで明るい未来を感じさせてくれるこちらのデザインに決定させていただきました。ロゴも見やすく気に入りました。ありがとうございました。
記載内容に追加をしていただきたいことがありますのでご相談に乗っていただければ幸いです。引き続きどうぞよろしくお願いいたします。

■ 提案者全員のお礼・コメント

この度は本当にたくさんの素敵なデザインをご応募いただきましてありがとうございました。
社員一同心より申し上げます。
どのデザインも甲乙つけがたい魅力がそれぞれにあり皆様の技術とセンスに感激しました。
またの機会がありました時にはまたお力を貸していただければ幸いです。
皆様のますますのご活躍をお祈りしつつお礼とさせていただきます。
ありがとうございました。

```html
<!DOCTYPE html>
<html lang="ja">
<head>
<meta charset="utf-8">
<title>謹賀新年 年賀状</title>
<link href="https://fonts.googleapis.com/css2?family=Shippori+Mincho+B1:wght@800&family=Noto+Sans+JP:wght@500;700&display=swap" rel="stylesheet">
<style>
  :root {
    --card-red: #c3161c;
    --card-red-deep: #a80f15;
    --gold: #d9ad45;
    --gold-light: #f0cf72;
    --ink-white: #ffffff;
  }
  html, body {
    margin: 0;
    padding: 0;
    width: 783px;
    height: 1200px;
    overflow: hidden;
    background: var(--card-red);
  }
  .card {
    position: relative;
    width: 783px;
    height: 1200px;
    background: radial-gradient(circle at 45% 35%, var(--card-red) 0%, var(--card-red) 55%, var(--card-red-deep) 100%);
    overflow: hidden;
    font-family: "Noto Sans JP", sans-serif;
    color: var(--ink-white);
  }
  .sparkle {
    position: absolute;
    border-radius: 50%;
    background: radial-gradient(circle, rgba(255,235,200,0.9) 0%, rgba(255,200,150,0.35) 30%, rgba(255,200,150,0) 70%);
  }
  .greeting-ring {
    position: absolute;
    left: 86px;
    top: 150px;
    width: 496px;
    height: 496px;
  }
  .title {
    position: absolute;
    left: 214px;
    top: 185px;
    width: 360px;
    display: grid;
    grid-template-columns: 1fr 1fr;
    row-gap: 0;
    font-family: "Shippori Mincho B1", serif;
    font-weight: 800;
    font-size: 150px;
    line-height: 148px;
    color: var(--gold);
    text-align: center;
  }
  .message {
    position: absolute;
    left: 0;
    width: 783px;
    top: 694px;
    margin: 0;
    text-align: center;
    padding-left: 92px;
    box-sizing: border-box;
    font-size: 22.5px;
    font-weight: 500;
    line-height: 35px;
    letter-spacing: 0.5px;
  }
  .date {
    position: absolute;
    left: 445px;
    top: 864px;
    margin: 0;
    font-size: 22px;
    font-weight: 700;
    letter-spacing: 1px;
  }
  .company {
    position: absolute;
    left: 470px;
    top: 930px;
    width: 230px;
    display: flex;
    align-items: center;
    gap: 14px;
  }
  .company-mark {
    width: 20px;
    height: 20px;
    border: 3px solid var(--ink-white);
    flex: none;
  }
  .company-name {
    font-size: 25px;
    font-weight: 700;
    line-height: 44px;
    letter-spacing: 1px;
  }
  .gold-strokes {
    position: absolute;
    left: 0;
    bottom: 0;
    width: 783px;
    height: 140px;
    background: linear-gradient(180deg, rgba(217,173,69,0) 0%, rgba(217,173,69,0.55) 35%, var(--gold) 75%, var(--gold-light) 100%);
  }
</style>
</head>
<body>
  <main class="card">
    <div class="sparkle" role="img" aria-label="きらめく星の装飾" style="left:60px;top:25px;width:90px;height:90px;"></div>
    <div class="sparkle" role="img" aria-label="きらめく星の装飾" style="left:500px;top:110px;width:120px;height:120px;"></div>
    <div class="sparkle" role="img" aria-label="きらめく星の装飾" style="left:640px;top:380px;width:110px;height:110px;"></div>
    <div class="sparkle" role="img" aria-label="きらめく星の装飾" style="left:640px;top:520px;width:100px;height:100px;"></div>
    <div class="sparkle" role="img" aria-label="きらめく星の装飾" style="left:50px;top:555px;width:90px;height:90px;"></div>
    <div class="sparkle" role="img" aria-label="きらめく星の装飾" style="left:680px;top:760px;width:80px;height:80px;"></div>
    <div class="sparkle" role="img" aria-label="きらめく星の装飾" style="left:560px;top:835px;width:70px;height:70px;"></div>

    <svg class="greeting-ring" viewBox="0 0 496 496" aria-hidden="true">
      <circle cx="248" cy="248" r="236" fill="none" stroke="var(--gold)" stroke-width="10"/>
      <circle cx="248" cy="248" r="214" fill="none" stroke="var(--gold)" stroke-width="8"/>
    </svg>

    <h1 class="title" aria-label="謹賀新年" style="margin:0;">
      <span>謹</span><span>賀</span><span>新</span><span>年</span>
    </h1>

    <p class="message">
      旧年中はひとかたならぬご厚情を賜り<br>
      誠にありがとうございました。<br>
      本年も変わりませず、よろしくお願いいたします。<br>
      皆様のご健康とご多幸をお祈り申し上げます。
    </p>

    <p class="date">令和五年 元旦</p>

    <div class="company">
      <span class="company-mark"></span>
      <span class="company-name">株式会社<br>桜井自動車</span>
    </div>

    <div class="gold-strokes" role="img" aria-label="金色の筆致による装飾帯"></div>
  </main>
</body>
</html>
```